Norvessa Imports Busisness cards and logo

Norvessa imports is a brand new wholesale company located in Londonderry, New Hampshire dedicated to finding unique products from around the world.
Licensed to sell wine and spirits in the state and also authorized distributors of Velvet Lantern Design, a manufacturer of girls and women shoes. Other products that we are currently trying to import are cheese and frozen food from Spain.
We would like a design that portraits our diversity of products and wholesale capabilities

Reason: Still undecided. Waiting for more feedback from the poll Thanks

```html
<!DOCTYPE html>
<html lang="en">
<head>
<meta charset="utf-8">
<title>Norvessa Imports – Business Card</title>
<link href="https://fonts.googleapis.com/css2?family=Exo+2:wght@400;500;600&display=swap" rel="stylesheet">
<style>
  :root {
    --page: #e6e7e6;
    --card-light: #ffffff;
    --card-shade: #e9eae9;
    --ink: #2f3230;
    --ink-soft: #4a4d4b;
    --green: #4f9a2f;
    --green-light: #7ab648;
    --grey-band: #8a8c8b;
  }
  * { margin: 0; padding: 0; box-sizing: border-box; }
  html, body { width: 1200px; height: 900px; overflow: hidden; }
  body {
    background: var(--page);
    font-family: "Exo 2", sans-serif;
    color: var(--ink);
    position: relative;
  }
  .card {
    position: absolute;
    left: 267px;
    width: 665px;
    height: 380px;
    background: radial-gradient(ellipse at 60% 40%, var(--card-light) 0%, var(--card-shade) 100%);
    box-shadow: 0 6px 18px rgba(0,0,0,0.18);
    overflow: hidden;
  }
  .card--back { top: 40px; }
  .card--front { top: 480px; }

  .brand {
    position: absolute;
    display: flex;
    align-items: center;
    gap: 12px;
    white-space: nowrap;
  }
  .brand__dot {
    flex: none;
    width: 46px; height: 46px;
    border-radius: 50%;
    background: var(--green);
  }
  .brand__name {
    font-weight: 600;
    font-size: 40px;
    color: var(--green);
    letter-spacing: 0.5px;
    white-space: nowrap;
  }
  .card--back .brand { left: 50%; top: 50%; transform: translate(-50%, -50%); }
  .card--front .brand { left: 282px; top: 118px; }
  .card--front .brand__name { font-size: 36px; }
  .card--front .brand__dot { width: 42px; height: 42px; }

  .card__swoosh { position: absolute; inset: 0; }

  .contact {
    position: absolute;
    left: 44px;
    top: 40px;
    font-size: 17px;
    font-weight: 500;
    color: var(--ink);
  }
  .contact__address { line-height: 24px; margin-bottom: 12px; letter-spacing: 0.6px; }
  .contact__row {
    display: flex;
    align-items: center;
    gap: 12px;
    height: 31px;
    letter-spacing: 1px;
    white-space: nowrap;
  }
  .contact__row--email { font-size: 15px; letter-spacing: 0.3px; }
  .contact__icon { width: 18px; height: 18px; flex: none; }

  .person {
    position: absolute;
    right: 44px;
    top: 196px;
    text-align: right;
    text-transform: uppercase;
    white-space: nowrap;
  }
  .person__name { font-size: 22px; font-weight: 500; letter-spacing: 2px; color: var(--ink); line-height: 28px; }
  .person__role { font-size: 14px; font-weight: 500; letter-spacing: 2px; color: var(--ink-soft); line-height: 20px; margin-top: 2px; }
</style>
</head>
<body>

  <section class="card card--back">
    <div class="brand">
      <span class="brand__dot"></span>
      <span class="brand__name">Norvessa Imports</span>
    </div>
  </section>

  <section class="card card--front">
    <svg class="card__swoosh" viewBox="0 0 665 380" width="665" height="380" aria-hidden="true">
      <defs>
        <linearGradient id="greenFill" x1="0" y1="0" x2="1" y2="0">
          <stop offset="0" stop-color="#3f8a2a"/>
          <stop offset="1" stop-color="#7ab648"/>
        </linearGradient>
      </defs>
      <path d="M0 252 C 330 256 540 270 665 350" fill="none" stroke="var(--grey-band)" stroke-width="9"/>
      <path d="M0 264 C 340 268 550 284 665 362" fill="none" stroke="var(--green-light)" stroke-width="3"/>
      <path d="M0 278 C 350 282 560 300 665 380 L 0 380 Z" fill="url(#greenFill)"/>
    </svg>

    <div class="contact">
      <p class="contact__address">041.12th floor,Plaza<br>Harbor Road NVS</p>
      <p class="contact__row">
        <svg class="contact__icon" viewBox="0 0 20 20"><path d="M5 2 L8 2 L9 6 L7 8 C8 11 9 12 12 13 L14 11 L18 12 L18 15 C18 17 16 18 14 18 C8 17 3 12 2 6 C2 4 3 2 5 2 Z" fill="var(--green)"/></svg>
        012 555 0147
      </p>
      <p class="contact__row">
        <svg class="contact__icon" viewBox="0 0 20 20"><rect x="5" y="1" width="10" height="18" rx="2" fill="none" stroke="var(--green)" stroke-width="2"/><rect x="7" y="4" width="6" height="10" fill="var(--green)"/></svg>
        012 555 0147
      </p>
      <p class="contact__row">
        <svg class="contact__icon" viewBox="0 0 20 20"><rect x="2" y="8" width="16" height="10" fill="var(--green)"/><rect x="5" y="2" width="10" height="7" fill="none" stroke="var(--green)" stroke-width="2"/><rect x="5" y="11" width="3" height="2" fill="#fff"/><rect x="10" y="11" width="3" height="2" fill="#fff"/><rect x="5" y="14" width="3" height="2" fill="#fff"/><rect x="10" y="14" width="3" height="2" fill="#fff"/></svg>
        012 555 0147
      </p>
      <p class="contact__row contact__row--email">
        <svg class="contact__icon" viewBox="0 0 20 20"><rect x="1" y="4" width="18" height="12" fill="var(--green)"/><path d="M1 4 L10 11 L19 4" fill="none" stroke="#fff" stroke-width="1.5"/></svg>
        hello@norvessa.com
      </p>
    </div>

    <div class="brand">
      <span class="brand__dot"></span>
      <span class="brand__name">Norvessa Imports</span>
    </div>

    <div class="person">
      <p class="person__name">Daniel Corvey</p>
      <p class="person__role">Financial Advisor</p>
    </div>
  </section>

</body>
</html>
```